LinkedIn Launch Campaign - Info Graphics / Email Template

mapleway Travel is a full end to end travel management solution for companies spending between 50k - 8 million a year on travel.

Our software helps companies manage their travel spend and helps employees book their business travel easily.

We are planning to launch our product via LinkedIn in Jan. The launch campaign will run for 2 weeks which we will be posting 6 info-graphics that outline some of the key functionality of our product. These info-graphics need to carry a similar feeling/look and theme as our website (maplewaytravel.com.au).

After the campaign is completed we will then shoot off a HTML email to people to provide more details about us and if they need more info they can get in contact with us.

The info-graphics need to be witty, fun, smart and catchy... They really need to grab peoples attention. The graphics need to marry in with the copy and statement.

Please see below the copy for each graphics, we have text for each graphic but we are unsure if we place the text in the graphic or have this typed into the post on linkedin.

So we will need 6 Info-Graphics designed and 2 email template designs.

Headline Statement – This will be posted regularly so it needs to awesome and very eye catching.

*mapleway Travel. Ridiculously easy low cost business travel
Budget- Book – Manage

================================================

*Stop Killing Time - Streamline Travel

mapleway Travel. Ridiculously easy low cost business travel
Budget- Book – Manage
TEXT:
Tired of manually managing every little trip detail from multiple platforms? Consolidate all your travel details in one place.

*Save That Cash for Your Bottom Line

Budget- Book – Manage

TEXT:
No more shopping around for deals. Get the most reasonable offers with super low fees on everything from flights, hotel accommodations to vehicle rentals in one click.

* Know What You Spend at a Glance

Budget- Book – Manage
TEXT:
Budget in real-time without the fear of overspending. Track spending, view reports, upload forecasts, and much more from our easy-to-read dashboard.

*Achieve Seamless Travel Compliance

Budget- Book – Manage

TEXT:
In real time track compliance to your travel policy for a stress-free relationship with employees. Be transparent with your employees, set spending limits, and always be audit ready.

=================================================

*Skip the Learning Curve
Budget- Book – Manage

TEXT:
No more boring training sessions! Employees can start using our intuitive interface right away. Spend less time learning a new platform and more time using it.

Project Deadline Extended Reason: We want to extend the deadline to give people more time to work on our project. Also due to the time of year we understand people may be away and will need more time. Added Wednesday, December 28, 2016

Target Market(s)

Target Audience
Mainly Accountants, VP Finance, Bookkeepers, Finance Manager, Senior Management

Industry/Entity Type

Business

Font styles to use
Serif
Sans Serif

Requirements
Must have
• We must use the same feeling / theme / look / as our website.
• It needs to be witty/ modern / smart / fun
• Needs to be simple and clean, like our website.
• Graphics need to connect with the statement / words.
• Needs to be eye catching/ stand out. We like our current colour pallet on our website but we can vary from it so the images are individual and not all the same

```html
<!DOCTYPE html>
<html lang="en">
<head>
<meta charset="utf-8">
<title>mapleway Travel – Email</title>
<link href="https://fonts.googleapis.com/css2?family=Berkshire+Swash&family=Montserrat:ital,wght@0,300;0,400;0,600;1,400&display=swap" rel="stylesheet">
<style>
  :root {
    --page-bg: #d4d4d4;
    --panel-bg: #e4e7ec;
    --sky-top: #eef0f4;
    --sky-bottom: #dfe3ea;
    --navy: #1f2f48;
    --ink: #2c3442;
    --muted: #6f737a;
    --ring: #b3b6bb;
    --accent: #4cc3ee;
    --card-bg: #f6f8fb;
  }
  * { margin: 0; padding: 0; box-sizing: border-box; }
  html, body { width: 1200px; height: 2462px; overflow: hidden; }
  body {
    background: var(--page-bg);
    font-family: "Montserrat", Arial, sans-serif;
    color: var(--ink);
    position: relative;
  }
  .email {
    position: absolute; left: 194px; top: 121px;
    width: 814px; height: 2223px;
    background: var(--panel-bg);
    overflow: hidden;
  }
  .sky {
    position: absolute; left: 0; top: 0; width: 814px; height: 412px;
    background:
      radial-gradient(ellipse 180px 90px at 50% 24%, #ffffff 0%, rgba(255,255,255,0) 100%),
      radial-gradient(ellipse 110px 90px at 4% 40%, #ffffff 0%, rgba(255,255,255,0) 100%),
      radial-gradient(ellipse 130px 110px at 98% 35%, #ffffff 0%, rgba(255,255,255,0) 100%),
      radial-gradient(ellipse 60px 30px at 81% 13%, #ffffff 0%, rgba(255,255,255,0) 100%),
      linear-gradient(180deg, var(--sky-top), var(--sky-bottom));
  }
  .side-cloud {
    position: absolute; border-radius: 50%;
    background: radial-gradient(ellipse at center, rgba(255,255,255,.55), rgba(255,255,255,0) 70%);
  }
  .brand-mark {
    position: absolute; left: 0; width: 814px; top: 92px; height: 36px;
    display: flex; justify-content: center; align-items: center; gap: 12px;
    font-weight: 600; font-size: 26px; color: var(--navy);
  }
  .brand-mark .dot { width: 26px; height: 26px; border-radius: 50%; background: var(--accent); }

  .hero { position: absolute; left: 0; top: 0; width: 814px; height: 412px; text-align: center; }
  .hero-title {
    position: absolute; left: 0; width: 814px; top: 211px;
    font-weight: 300; font-size: 42px; line-height: 52px; color: var(--ink);
  }
  .hero-tagline {
    position: absolute; left: 0; width: 814px; top: 263px;
    font-weight: 300; font-size: 23px; line-height: 30px; color: var(--ink);
  }
  .hero-pillars {
    position: absolute; left: 0; width: 814px; top: 303px;
    font-weight: 600; font-size: 17px; line-height: 26px; color: var(--navy);
  }

  .feature { position: absolute; left: 0; width: 814px; height: 250px; text-align: center; }
  .feature-title {
    position: absolute; left: 0; width: 814px; top: 0;
    font-family: "Berkshire Swash", Georgia, serif;
    font-weight: 400; font-size: 37px; line-height: 44px; color: var(--navy);
  }
  .feature-tagline {
    position: absolute; left: 0; width: 814px; top: 52px;
    font-weight: 300; font-size: 22px; line-height: 32px; color: var(--ink);
  }
  .feature-pillars {
    position: absolute; left: 0; width: 814px; top: 93px;
    font-weight: 600; font-size: 17px; line-height: 26px; color: var(--navy);
  }
  .card { position: absolute; text-align: left; }
  .card-shape { position: absolute; inset: 0; }
  .card-text {
    position: relative;
    font-style: italic; font-size: 16px; line-height: 26px; color: var(--ink);
  }
  .card-shadow {
    position: absolute; left: 110px; bottom: -14px; width: 200px; height: 16px;
    background: radial-gradient(ellipse at center, rgba(20,25,35,.55), rgba(20,25,35,0) 70%);
  }

  .social {
    position: absolute; left: 0; width: 814px; top: 2023px;
    display: flex; justify-content: center; gap: 10px;
  }
  .social span { width: 42px; height: 42px; border-radius: 50%; border: 2px solid var(--ring); }
  .footer-links {
    position: absolute; left: 0; width: 814px; top: 2085px; text-align: center;
    font-weight: 600; font-size: 14px; line-height: 20px; color: var(--muted);
  }
  .footer-links i { font-style: normal; margin: 0 8px; }
  .rights {
    position: absolute; left: 0; width: 814px; top: 2124px; text-align: center;
    font-size: 22px; line-height: 30px; font-weight: 400; color: var(--ink);
  }
  .footer-brand {
    position: absolute; left: 656px; top: 2156px; height: 30px;
    display: flex; align-items: center; gap: 8px;
    font-weight: 600; font-size: 20px; color: var(--navy);
  }
  .footer-brand .dot { width: 20px; height: 20px; border-radius: 50%; background: var(--accent); }
  .footer-bar { position: absolute; left: 678px; top: 2204px; width: 103px; height: 19px; background: var(--navy); }
</style>
</head>
<body>
  <main class="email">
    <div class="sky" role="img" aria-label="Soft white clouds in a pale sky with a small plane"></div>
    <div class="side-cloud" role="img" aria-label="Faint cloud" style="left:-120px;top:560px;width:300px;height:260px"></div>
    <div class="side-cloud" role="img" aria-label="Faint cloud" style="left:620px;top:700px;width:300px;height:240px"></div>
    <div class="side-cloud" role="img" aria-label="Faint cloud" style="left:-140px;top:1300px;width:320px;height:280px"></div>
    <div class="side-cloud" role="img" aria-label="Faint cloud" style="left:640px;top:1460px;width:280px;height:240px"></div>
    <div class="side-cloud" role="img" aria-label="Faint cloud" style="left:-120px;top:1900px;width:320px;height:260px"></div>

    <div class="brand-mark"><span class="dot"></span>mapleway</div>

    <header class="hero">
      <h1 class="hero-title">mapleway Travel.</h1>
      <p class="hero-tagline">Ridiculously easy low cost business travel</p>
      <p class="hero-pillars">Budget- Book – Manage</p>
    </header>

    <section class="feature" style="top:407px">
      <h2 class="feature-title">Stop Killing Time - Streamline Travel</h2>
      <p class="feature-tagline">mapleway Travel. Ridiculously easy low cost business travel</p>
      <p class="feature-pillars">Budget- Book – Manage</p>
      <div class="card" style="left:88px;top:125px;width:638px;height:94px">
        <svg class="card-shape" width="638" height="94" viewBox="0 0 638 94">
          <polygon points="30,2 638,2 610,94 0,94" fill="var(--card-bg)"/>
          <polyline points="30,2 638,2 610,94" fill="none" stroke="var(--accent)" stroke-width="3"/>
        </svg>
        <div class="card-shadow"></div>
        <p class="card-text" style="padding:20px 38px 0 53px">Tired of manually managing every little trip detail from multiple platforms? Consolidate all your travel details in one place.</p>
      </div>
    </section>

    <section class="feature" style="top:719px">
      <h2 class="feature-title">Save That Cash for Your Bottom Line</h2>
      <p class="feature-tagline">mapleway Travel. Ridiculously easy low cost business travel</p>
      <p class="feature-pillars">Budget- Book – Manage</p>
      <div class="card" style="left:67px;top:125px;width:693px;height:112px">
        <svg class="card-shape" width="693" height="112" viewBox="0 0 693 112">
          <polygon points="32,2 693,2 664,112 0,112" fill="var(--card-bg)"/>
          <polyline points="32,2 693,2 664,112" fill="none" stroke="var(--accent)" stroke-width="3"/>
        </svg>
        <div class="card-shadow"></div>
        <p class="card-text" style="padding:18px 40px 0 46px">No more shopping around for deals. Get the most reasonable offers with super low fees on everything from flights, hotel accommodations to vehicle rentals in one click.</p>
      </div>
    </section>

    <section class="feature" style="top:1026px">
      <h2 class="feature-title">Know What You Spend at a Glance</h2>
      <p class="feature-tagline">mapleway Travel. Ridiculously easy low cost business travel</p>
      <p class="feature-pillars">Budget- Book – Manage</p>
      <div class="card" style="left:88px;top:125px;width:638px;height:112px">
        <svg class="card-shape" width="638" height="112" viewBox="0 0 638 112">
          <polygon points="30,2 638,2 610,112 0,112" fill="var(--card-bg)"/>
          <polyline points="30,2 638,2 610,112" fill="none" stroke="var(--accent)" stroke-width="3"/>
        </svg>
        <div class="card-shadow"></div>
        <p class="card-text" style="padding:18px 38px 0 53px">Budget in real-time without the fear of overspending. Track spending, view reports, upload forecasts, and much more from our easy-to-read dashboard.</p>
      </div>
    </section>

    <section class="feature" style="top:1338px">
      <h2 class="feature-title">Achieve Seamless Travel Compliance</h2>
      <p class="feature-tagline">mapleway Travel. Ridiculously easy low cost business travel</p>
      <p class="feature-pillars">Budget- Book – Manage</p>
      <div class="card" style="left:67px;top:125px;width:693px;height:112px">
        <svg class="card-shape" width="693" height="112" viewBox="0 0 693 112">
          <polygon points="32,2 693,2 664,112 0,112" fill="var(--card-bg)"/>
          <polyline points="32,2 693,2 664,112" fill="none" stroke="var(--accent)" stroke-width="3"/>
        </svg>
        <div class="card-shadow"></div>
        <p class="card-text" style="padding:18px 40px 0 46px">In real time track compliance to your travel policy for a stress-free relationship with employees. Be transparent with your employees, set spending limits, and always be audit ready.</p>
      </div>
    </section>

    <section class="feature" style="top:1643px">
      <h2 class="feature-title">Skip the Learning Curve</h2>
      <p class="feature-tagline">mapleway Travel. Ridiculously easy low cost business travel</p>
      <p class="feature-pillars">Budget- Book – Manage</p>
      <div class="card" style="left:67px;top:125px;width:693px;height:112px">
        <svg class="card-shape" width="693" height="112" viewBox="0 0 693 112">
          <polygon points="32,2 693,2 664,112 0,112" fill="var(--card-bg)"/>
          <polyline points="32,2 693,2 664,112" fill="none" stroke="var(--accent)" stroke-width="3"/>
        </svg>
        <div class="card-shadow"></div>
        <p class="card-text" style="padding:18px 40px 0 46px">No more boring training sessions! Employees can start using our intuitive interface right away. Spend less time learning a new platform and more time using it.</p>
      </div>
    </section>

    <footer>
      <div class="social"><span></span><span></span><span></span></div>
      <p class="footer-links">Privacy<i>I</i>T&amp;C's<i>I</i>Contact<i>I</i>Sign Up</p>
      <p class="rights">All rights reserved mapleway, 2017.</p>
      <div class="footer-brand"><span class="dot"></span>mapleway</div>
      <div class="footer-bar"></div>
    </footer>
  </main>
</body>
</html>
```